Business Card Design for general contractor or developer

General Contractors. We build new buildings as well as redesign and/or remodel existing buildings. Mostly residential, but we want to expand to commercial as well, so we want the design not to be residential specific.We want the design to be modern, but necessarily minimalistic. A monogram type is also a consideration, but would like to see all ideas.

Target Market(s)

Real estate investors, homeowners, future homeowners, commercial building owners

Industry/Entity Type

Contractor

Contact Information for Business Card

BRIMCOVE Developers Corp, 2917 NE 88th Avenue Suite 412 Coral Springs, FL 33071, Darren Kopec, (305) 555-0148, darren@brimcovedev.example

Font styles to use
Other font styles liked:
• Modern type font

Requirements
Must have
• Must be modern looking
Nice to have
• Metallic type or a standout feature
Should not have
• Tools, floorplans

```html
<!DOCTYPE html>
<html lang="en">
<head>
<meta charset="utf-8">
<title>BRIMCOVE Developers Corp – Business Card</title>
<link rel="stylesheet" href="https://fonts.googleapis.com/css2?family=Lato:wght@400;700&display=swap">
<style>
  :root {
    --canvas: #e9e7e3;
    --card-white: #ffffff;
    --forest: #0f4a39;
    --ink: #3a3a3a;
    --muted: #555555;
    --on-forest: #ffffff;
    --grey-light: #9a9a9a;
    --grey-mid: #858585;
    --grey-dark: #6f6f6f;
  }
  * { box-sizing: border-box; margin: 0; padding: 0; }
  html, body { width: 1200px; height: 1023px; overflow: hidden; }
  body {
    background: var(--canvas);
    font-family: "Lato", sans-serif;
    display: flex;
    flex-direction: column;
    align-items: center;
    justify-content: center;
    gap: 31px;
  }
  .card {
    position: relative;
    width: 840px;
    height: 480px;
    border-radius: 24px;
    overflow: hidden;
    box-shadow: 0 4px 14px rgba(0,0,0,0.15);
  }
  /* Front */
  .card-front { background: var(--card-white); }
  .front-band { position: absolute; inset: 0; }
  .brand {
    position: absolute;
    display: flex;
    align-items: center;
    gap: 14px;
    color: var(--forest);
    font-weight: 700;
    white-space: nowrap;
  }
  .brand-dot {
    border-radius: 50%;
    background: var(--forest);
    flex: none;
  }
  .card-front .brand { top: 82px; right: 60px; font-size: 30px; }
  .card-front .brand-dot { width: 26px; height: 26px; }
  .address {
    position: absolute;
    right: 40px;
    bottom: 40px;
    text-align: right;
    color: var(--on-forest);
    font-size: 18px;
    line-height: 1.45;
    white-space: nowrap;
  }
  .person {
    position: absolute;
    left: 60px;
    bottom: 62px;
    color: var(--ink);
  }
  .person-name { font-size: 24px; font-weight: 700; color: var(--forest); }
  .person-title { font-size: 19px; color: var(--muted); margin-top: 4px; margin-bottom: 22px; }
  .contact-list { list-style: none; font-size: 19px; color: var(--muted); }
  .contact-list li { display: flex; align-items: center; gap: 10px; line-height: 1.5; }
  .contact-icon { width: 17px; height: 17px; flex: none; }
  /* Back */
  .card-back {
    background: linear-gradient(160deg, var(--grey-light) 0%, var(--grey-mid) 45%, var(--grey-dark) 100%);
  }
  .card-back .brand {
    top: 50%; left: 50%;
    transform: translate(-50%, -50%);
    font-size: 44px;
  }
  .card-back .brand-dot { width: 40px; height: 40px; }
</style>
</head>
<body>

  <section class="card card-front">
    <svg class="front-band" viewBox="0 0 840 480" aria-hidden="true">
      <path d="M380 480 C 520 400, 680 260, 840 140 L 840 480 Z" fill="var(--forest)"/>
    </svg>

    <div class="brand"><span class="brand-dot"></span>BRIMCOVE Developers Corp</div>

    <p class="address">2917 NE 88th Avenue Suite 412<br>Coral Springs, FL 33071</p>

    <div class="person">
      <p class="person-name">Darren Kopec</p>
      <p class="person-title">Owner</p>
      <ul class="contact-list">
        <li>
          <svg class="contact-icon" viewBox="0 0 24 24"><path fill="var(--muted)" d="M6.6 10.8a15 15 0 0 0 6.6 6.6l2.2-2.2c.3-.3.7-.4 1-.2 1.1.4 2.3.6 3.6.6.6 0 1 .4 1 1V20c0 .6-.4 1-1 1A17 17 0 0 1 3 4c0-.6.4-1 1-1h3.5c.6 0 1 .4 1 1 0 1.3.2 2.5.6 3.6.1.3 0 .7-.2 1z"/></svg>
          (305) 555-0148
        </li>
        <li>
          <svg class="contact-icon" viewBox="0 0 24 24"><rect x="2" y="5" width="20" height="14" rx="1" fill="var(--muted)"/><path d="M3 6l9 7 9-7" stroke="#fff" stroke-width="1.6" fill="none"/></svg>
          darren@brimcovedev.example
        </li>
        <li>
          <svg class="contact-icon" viewBox="0 0 24 24"><g fill="none" stroke="var(--muted)" stroke-width="1.8"><circle cx="12" cy="12" r="9.5"/><ellipse cx="12" cy="12" rx="4" ry="9.5"/><path d="M2.5 12h19M4 7h16M4 17h16"/></g></svg>
          www.brimcovedev.example
        </li>
      </ul>
    </div>
  </section>

  <section class="card card-back">
    <div class="brand"><span class="brand-dot"></span>BRIMCOVE Developers Corp</div>
  </section>

</body>
</html>
```